E-mail Design for offering customers a unique discount code

A custom email design matching our website theme and colours (brightwaylessons.com) similar to the plan attached, can we have the below points grabbing the viewers attention is some way:<br/>- The Quickest Way To Get Your Driving Licence<br/>- Local Driving Instructor With Home Pickup<br/>- We Can Start You Within 2 Weeks In Most Cases<br/>- We Offer Courses For All Experience & Abilities<br/>- The Average Cost Of Weekly Lessons Is More Expensive <br/>- The RTQB Recommend 47 Hours With Weekly Lessons, We Only Recommend 30-35 Hours With An Intensive Course<br/><br/>SAVE TIME, SAVE MONEY & BOOK NOW WITH BRIGHTWAY LESSONS<br/><br/>Also the main aim of the e-mail is to highlight the offer and discount code, this would be good if it could flash at all
Target Market(s)
17-35 year olds
Font styles to use
Colors
Designer to choose colors to be used in the design.
Requirements
Must have
- colours and them from website
Nice to have
- flashing discount and discount code

```html
<!DOCTYPE html>
<html lang="en">
<head>
<meta charset="utf-8">
<title>Brightway Lessons – £50 Off Your Driving Course</title>
<link rel="stylesheet" href="https://fonts.googleapis.com/css2?family=Poppins:wght@400;500;600;700;800;900&display=swap">
<style>
  :root {
    --navy: #173b5f;
    --navy-deep: #12304f;
    --sky-top: #d3e3ef;
    --sky-bottom: #e6eff6;
    --nav-bg: #ffffff;
    --offer-blue: #0aa2ee;
    --orange: #f7903a;
    --yellow: #fdc400;
    --code-yellow: #ffe600;
    --purple: #a61dc8;
    --cyan: #0bb6e6;
    --white: #ffffff;
    --text-dark: #1e2b3a;
    --photo-a: #8d8f92;
    --photo-b: #6e7378;
    --tab-edge: #2f6fb0;
    --social-one: #3b5ea8;
    --social-two: #2aa6e8;
    --social-three: #2a7ab7;
  }
  * { box-sizing: border-box; margin: 0; padding: 0; }
  html, body { width: 1200px; height: 2885px; overflow: hidden; }
  body { font-family: "Poppins", sans-serif; color: var(--white); background: var(--navy); }
  .email { position: relative; width: 1200px; height: 2885px; overflow: hidden; }

  .top-bar { height: 81px; background: var(--navy); display: flex; align-items: center; justify-content: center; font-size: 22px; font-weight: 500; }

  .masthead { position: relative; height: 237px; background: linear-gradient(180deg, var(--sky-top), var(--sky-bottom)); }
  .masthead .skyline { position: absolute; left: 0; right: 0; bottom: 0; height: 150px; background: linear-gradient(180deg, rgba(190,208,222,0) 0%, rgba(190,208,222,0.7) 100%); }
  .brand-tab { position: absolute; left: 300px; top: 0; width: 600px; height: 138px; }
  .brand-tab svg { position: absolute; inset: 0; }
  .brand { position: absolute; inset: 0; display: flex; align-items: center; justify-content: center; gap: 22px; padding-bottom: 8px; }
  .brand-mark { width: 64px; height: 64px; border-radius: 10px; background: var(--white); }
  .brand-name { font-weight: 700; font-size: 42px; line-height: 1; color: var(--white); letter-spacing: 1px; }

  .main-nav { height: 106px; background: var(--nav-bg); display: flex; align-items: center; justify-content: center; gap: 30px; font-size: 27px; font-weight: 600; color: var(--text-dark); letter-spacing: 0.5px; }
  .main-nav .sep { font-weight: 400; }

  .offer { position: relative; height: 643px; background: var(--offer-blue); text-align: center; overflow: hidden; }
  .offer-badge { position: absolute; left: 254px; top: -337px; width: 692px; height: 692px; border-radius: 50%; background: var(--orange); border: 17px solid var(--white); }
  .offer-badge .amount { position: absolute; left: 0; right: 0; top: 346px; display: flex; justify-content: center; align-items: flex-end; font-weight: 900; line-height: 0.85; text-shadow: 5px 6px 0 rgba(0,0,0,0.55); }
  .amount .pound { font-size: 78px; align-self: flex-start; margin-top: 10px; }
  .amount .value { font-size: 190px; letter-spacing: -6px; }
  .amount .off { font-size: 76px; margin-left: 6px; margin-bottom: 4px; }
  .offer-badge .sub { position: absolute; left: 0; right: 0; top: 512px; font-size: 38px; font-weight: 500; letter-spacing: 1px; }
  .coupon-line { position: absolute; left: 0; right: 0; top: 386px; font-size: 53px; font-weight: 700; letter-spacing: 2px; }
  .coupon-code { color: var(--code-yellow); animation: flash 1.2s ease-in-out infinite; }
  @keyframes flash { 0%, 100% { opacity: 1; } 50% { opacity: 0.35; } }

  .btn { display: inline-flex; align-items: center; justify-content: center; width: 404px; height: 92px; border-radius: 46px; background: var(--yellow); color: var(--navy-deep); font-size: 38px; font-weight: 400; text-decoration: none; letter-spacing: 1px; }
  .offer .btn { position: absolute; left: 398px; top: 508px; }

  .reasons { position: relative; height: 852px; background: var(--purple); text-align: center; }
  .section-title { font-size: 54px; font-weight: 700; letter-spacing: 2px; }
  .reasons .section-title { position: absolute; left: 0; right: 0; top: 47px; }
  .selling-points { position: absolute; left: 177px; top: 200px; width: 890px; list-style: none; display: grid; grid-template-columns: 360px 440px; column-gap: 90px; row-gap: 26px; font-size: 24px; line-height: 1.3; font-weight: 500; }
  .selling-points li { position: relative; }
  .selling-points .left { text-align: right; }
  .selling-points .right { text-align: left; padding-left: 45px; }
  .selling-points .left::after, .selling-points .right::before { content: ""; position: absolute; top: 9px; width: 15px; height: 15px; border-radius: 50%; background: var(--white); }
  .selling-points .left::after { right: -34px; }
  .selling-points .right::before { left: 0; }
  .tagline { position: absolute; left: 0; right: 0; top: 632px; font-size: 27px; font-weight: 700; letter-spacing: 1px; color: var(--code-yellow); }
  .reasons .btn { position: absolute; left: 398px; top: 725px; }

  .candidates { position: relative; height: 640px; background: var(--cyan); text-align: center; }
  .candidates .section-title { position: absolute; left: 0; right: 0; top: 38px; }
  .pass-photos { position: absolute; left: 156px; top: 184px; display: flex; gap: 12px; }
  .pass-photo { height: 384px; border: 9px solid var(--white); background: linear-gradient(160deg, var(--photo-a), var(--photo-b)); }

  .footer { height: 326px; background: var(--navy); text-align: center; padding-top: 56px; }
  .contact { font-size: 24px; font-weight: 500; }
  .contact .label { color: var(--yellow); font-weight: 600; }
  .contact .divider { margin: 0 26px; }
  .address { margin-top: 14px; font-size: 24px; font-weight: 500; }
  .social { margin-top: 58px; display: flex; justify-content: center; gap: 15px; }
  .social span { width: 75px; height: 75px; border-radius: 50%; }
  .social .one { background: var(--social-one); }
  .social .two { background: var(--social-two); }
  .social .three { background: var(--social-three); }
</style>
</head>
<body>
<div class="email">
  <div class="top-bar">View Web Version</div>

  <header class="masthead">
    <div class="skyline" role="img" aria-label="Faint city skyline silhouette"></div>
    <div class="brand-tab">
      <svg viewBox="0 0 600 138" width="600" height="138" aria-hidden="true">
        <path d="M0 0 H600 L560 110 Q552 132 528 132 H72 Q48 132 40 110 Z" fill="#2f6fb0"/>
        <path d="M14 0 H586 L550 102 Q543 122 520 122 H80 Q57 122 50 102 Z" fill="#173b5f"/>
      </svg>
      <div class="brand">
        <span class="brand-mark"></span>
        <span class="brand-name">BRIGHTWAY<br>LESSONS</span>
      </div>
    </div>
  </header>

  <nav class="main-nav">
    <span>ABOUT US</span><span class="sep">|</span>
    <span>PRICES</span><span class="sep">|</span>
    <span>FAQS</span><span class="sep">|</span>
    <span>PASS GALLERY</span>
  </nav>

  <section class="offer">
    <div class="offer-badge">
      <div class="amount"><span class="pound">£</span><span class="value">50</span><span class="off">OFF</span></div>
      <div class="sub">YOUR DRIVING COURSE</div>
    </div>
    <p class="coupon-line">USE COUPON CODE: <span class="coupon-code">JAN20</span></p>
    <a class="btn" href="#">BOOK ONLINE</a>
  </section>

  <section class="reasons">
    <h2 class="section-title">WHY YOU CHOOSE US</h2>
    <ul class="selling-points">
      <li class="left">The Quickest Way To Get Your Driving Licence</li>
      <li class="right">We Offer Courses For All Experience &amp; Abilities</li>
      <li class="left">Local Driving Instructor With Home Pickup</li>
      <li class="right">The Average Cost Of Weekly Lessons Is More Expensive</li>
      <li class="left">We Can Start You Within 2 Weeks In Most Cases</li>
      <li class="right">The RTQB Recommend 47 Hours With Weekly Lessons, We Only Recommend 30-35 Hours With An Intensive Course</li>
    </ul>
    <p class="tagline">SAVE TIME, SAVE MONEY &amp; BOOK NOW WITH BRIGHTWAY LESSONS</p>
    <a class="btn" href="#">BOOK ONLINE</a>
  </section>

  <section class="candidates">
    <h2 class="section-title">SUCCESSFULL CANDIDATES</h2>
    <div class="pass-photos">
      <div class="pass-photo" style="width:292px" role="img" aria-label="Photo of a successful learner holding a pass sign beside a tuition car"></div>
      <div class="pass-photo" style="width:288px" role="img" aria-label="Photo of a successful learner holding a pass certificate beside a tuition car"></div>
      <div class="pass-photo" style="width:288px" role="img" aria-label="Photo of a successful learner holding a pass certificate beside a tuition car"></div>
    </div>
  </section>

  <footer class="footer">
    <p class="contact"><span class="label">Phone:</span> 0161 555 0192<span class="divider">|</span><span class="label">Email:</span> office@brightwaylessons.com</p>
    <p class="address">Unit 7, East Court, Harbour Point, Mill Lane, M40 8QT</p>
    <div class="social" aria-label="Social links">
      <span class="one"></span><span class="two"></span><span class="three"></span>
    </div>
  </footer>
</div>
</body>
</html>
```